Medical IT Business with New logo needs a fresh stationary design

First time on sketch Harbor; Thought I would give it a go.
This project is for business cards alone but we have loads of design work that needs to take place in the immediate future.

We provide IT services to the Medical Industry and value ourselves as offering a premium product to the market.

I am after a fresh, clean design using full colour 2 sided cards which includes our current colour palettes from our logo.

Card's must include:
- Logo
- Slogan
- Name
- Adress
- Email
- Phone
- Fax
- Mobile

Target Market(s)

Surgeons, High Profile Medical Personnel

Industry/Entity Type

Business

Fonts, CMYK Colours and Logo files attached.

Requirements
Must have
• Card's must include:
• - Logo
• - Slogan
• - Name
• - Adress
• - Email
• - Phone
• - Fax
• - Mobile
Nice to have
• Needs to incorporate our colour palette (attached CMYK colours)
Should not have
• Black backgrounds. Black text ok.

```html
<!DOCTYPE html>
<html lang="en">
<head>
<meta charset="utf-8">
<title>Clinivera Systems – Business Cards</title>
<link rel="stylesheet" href="https://fonts.googleapis.com/css2?family=Open+Sans:wght@400;600;800&family=Arimo:wght@400&display=swap">
<style>
  :root {
    --bg: #e6e8eb;
    --brand-blue: #1a8cc8;
    --navy: #0f3f80;
    --sky: #5fb6e6;
    --white: #ffffff;
    --slogan: #7bbde4;
  }
  * { margin: 0; padding: 0; box-sizing: border-box; }
  html, body { width: 1200px; height: 950px; overflow: hidden; background: var(--bg); }
  .canvas { position: relative; width: 1200px; height: 950px; }

  .card {
    position: absolute; left: 250px; width: 700px; height: 400px;
    overflow: hidden; box-shadow: 0 6px 18px rgba(0,0,0,.18);
  }
  .card--front { top: 45px; background: var(--brand-blue); }
  .card--back { top: 505px; background: var(--white); }

  .brand { position: absolute; display: flex; align-items: center; }
  .brand__dot { border-radius: 50%; flex: none; }
  .brand__text { display: flex; flex-direction: column; }
  .brand__name {
    font-family: "Open Sans", sans-serif; font-weight: 800;
    font-size: 40px; line-height: 1; letter-spacing: .5px;
  }
  .brand__slogan {
    font-family: "Open Sans", sans-serif; font-weight: 600;
    font-size: 17px; margin-top: 6px; white-space: nowrap;
  }

  .card--front .brand { left: 110px; top: 120px; }
  .card--front .brand__dot { width: 130px; height: 130px; background: var(--white); margin-right: 18px; }
  .card--front .brand__name { color: var(--white); }
  .card--front .brand__slogan { color: var(--white); }
  .web-line {
    position: absolute; left: 0; right: 0; bottom: 62px; text-align: center;
    font-family: "Arimo", sans-serif; font-size: 18px; letter-spacing: 9px; color: var(--white);
  }

  .panel { position: absolute; left: 0; top: 0; width: 315px; height: 400px; background: var(--navy); }
  .card--back .brand { left: 255px; top: 108px; }
  .card--back .brand__dot { width: 120px; height: 120px; background: var(--brand-blue); margin-right: 16px; }
  .card--back .brand__name { color: var(--navy); font-size: 36px; }
  .card--back .brand__slogan { color: var(--slogan); font-size: 15px; }

  .contact {
    position: absolute; left: 42px; top: 44px; color: var(--white);
    font-family: "Arimo", sans-serif; font-size: 16px; line-height: 1.3;
  }
  .contact__name { color: var(--sky); font-size: 21px; text-transform: uppercase; }
  .contact__role { font-size: 15px; text-transform: uppercase; margin-bottom: 36px; }
  .contact__address { margin-bottom: 22px; }
  .contact__row { margin-bottom: 2px; }
  .contact__label { color: var(--sky); text-transform: uppercase; margin-right: 4px; }
</style>
</head>
<body>
<main class="canvas">
  <section class="card card--front" aria-label="Card front">
    <div class="brand">
      <span class="brand__dot"></span>
      <div class="brand__text">
        <span class="brand__name">CLINIVERA<br>SYSTEMS</span>
        <span class="brand__slogan">care connected every day</span>
      </div>
    </div>
    <p class="web-line">www.clinivera.com</p>
  </section>

  <section class="card card--back" aria-label="Card back">
    <div class="panel"></div>
    <div class="brand">
      <span class="brand__dot"></span>
      <div class="brand__text">
        <span class="brand__name">CLINIVERA<br>SYSTEMS</span>
        <span class="brand__slogan">care connected every day</span>
      </div>
    </div>
    <div class="contact">
      <p class="contact__name">Mara Ellison</p>
      <p class="contact__role">President</p>
      <p class="contact__address">4127 Harlow Avenue<br>Linden Heights, NY 10482</p>
      <p class="contact__row"><span class="contact__label">Phone:</span>555 0142 7781</p>
      <p class="contact__row"><span class="contact__label">Mob:</span>555 0186 3390</p>
      <p class="contact__row"><span class="contact__label">Fax:</span>555 0127 4615</p>
      <p class="contact__row"><span class="contact__label">Email:</span>mara@clinivera.com</p>
      <p class="contact__row"><span class="contact__label">Web:</span>www.clinivera.com</p>
    </div>
  </section>
</main>
</body>
</html>
```